Yacht, Boats, Watersports company needs a redesign of business card

Hello Designers!
We are a Boat dealership company that sells fun in the water, we sell boats, Yachts, Kayaks and also yacht WaterSport toys. We are looking to redesign our business cards in to something a little bit more sophisticated. in a way that we can make better use of our company colors. I'm attaching a zipped file containing the company 3 sets of company logo which one is an horizontal another one is a vertical and also a chromed 3d logo. Also is included two set of business cards that we use and also some designs that i think it's interesting. We use PMS 2026c Orange and PMS 7687C Blue. I would like to see at least two different options with the orange as accent and also using blue as an accent color. It's really important for the business cards to have a font option and size that is legible to most people. Our current website is wwww.corvellamarine.com. Please visit if you want to have a better feeling of the Boat dealership
You can send Single sided or double side options. We are now using single sided but we may be open for a double side option if we really like the design.
Target Market(s)
Marine, boat sales, yacht sales, water toys sales/
Contact Information for Business Card
Name: Dale Pritchett
Address: 718 West Halden Lane,
Dania Beach, FL 33019
Phone: 954-382-7146
Fax: 954:382-7139
Cell: 954-451-8320
Email: 212@corvellamarine.com
Website: corvellamarine.com
Requirements
Must have
- the current information of the business card provided.
logo
use the PMS Colors
Nice to have
- a touch of elegance and sophistication but simple
Should not have
- should not have any typography that is hard to read, the card should be simple but yet sophisticated.

```html
<!DOCTYPE html>
<html lang="en">
<head>
<meta charset="utf-8">
<title>Corvella Marine Business Card</title>
<link rel="stylesheet" href="https://fonts.googleapis.com/css2?family=Montserrat:wght@500;600;700&display=swap">
<style>
  :root {
    --navy: #26487a;
    --orange: #e85c2f;
    --paper: #ffffff;
    --backdrop: #ececec;
    --ink: #26487a;
  }
  * { margin: 0; padding: 0; box-sizing: border-box; }
  html, body { width: 842px; height: 1200px; overflow: hidden; }
  body {
    background: var(--backdrop);
    font-family: "Montserrat", Arial, sans-serif;
    position: relative;
  }
  .card {
    position: absolute;
    top: 385px;
    width: 263px;
    height: 430px;
    background: var(--paper);
    overflow: hidden;
  }
  .card--front { left: 98px; }
  .card--back { left: 481px; }
  .card__shapes { position: absolute; inset: 0; width: 100%; height: 100%; }
  .navy { fill: var(--navy); }
  .orange { fill: var(--orange); }

  .brand {
    position: absolute;
    left: 40px;
    top: 96px;
    display: flex;
    align-items: center;
    gap: 8px;
  }
  .brand__dot {
    width: 14px; height: 14px; border-radius: 50%;
    background: var(--orange);
  }
  .brand__name {
    font-weight: 700;
    font-size: 17px;
    color: var(--navy);
    letter-spacing: 0.5px;
  }

  .holder-name {
    position: absolute;
    left: 40px;
    top: 184px;
    font-weight: 500;
    font-size: 20px;
    letter-spacing: 0.3px;
    color: var(--ink);
    white-space: nowrap;
  }
  .contact-list { list-style: none; }
  .contact {
    position: absolute;
    left: 41px;
    display: flex;
    align-items: center;
    width: 215px;
  }
  .contact__icon {
    flex: none;
    width: 20px; height: 20px;
    background: var(--orange);
    display: flex; align-items: center; justify-content: center;
  }
  .contact__icon svg { width: 12px; height: 12px; fill: #fff; }
  .contact__text {
    margin-left: 15px;
    font-size: 9.4px;
    font-weight: 500;
    line-height: 12.5px;
    color: var(--ink);
    white-space: nowrap;
  }
  .contact--address { top: 232px; }
  .contact--phone { top: 258px; }
  .contact--fax { top: 286px; }
  .contact--cell { top: 313px; }
  .contact--email { top: 341px; }
  .contact--web { top: 368px; }
  .contact--address .contact__text { margin-top: 1px; }

  .back-mark {
    position: absolute;
    left: 105px;
    top: 88px;
    width: 52px; height: 52px;
    border-radius: 50%;
    border: 5px solid var(--orange);
  }
  .back-name {
    position: absolute;
    left: 131px;
    top: 160px;
    transform-origin: 0 0;
    transform: rotate(90deg) translateY(-50%);
    font-weight: 700;
    font-size: 18px;
    letter-spacing: 0.3px;
    color: var(--navy);
    white-space: nowrap;
  }
</style>
</head>
<body>

<section class="card card--front" aria-label="Business card front">
  <svg class="card__shapes" viewBox="0 0 263 430" aria-hidden="true">
    <polygon class="navy" points="62,0 263,0 201,80"/>
    <polygon class="orange" points="263,0 263,117 201,80"/>
    <polygon class="orange" points="211,391 263,360 263,430 240,430"/>
    <polygon class="navy" points="145,430 211,391 240,430"/>
  </svg>

  <div class="brand">
    <span class="brand__dot"></span>
    <span class="brand__name">Corvella Marine</span>
  </div>

  <h1 class="holder-name">DALE PRITCHETT</h1>

  <ul class="contact-list">
    <li class="contact contact--address">
      <span class="contact__icon"><svg viewBox="0 0 24 24"><path d="M12 2a7 7 0 0 0-7 7c0 5 7 13 7 13s7-8 7-13a7 7 0 0 0-7-7zm0 9.5A2.5 2.5 0 1 1 12 6.5a2.5 2.5 0 0 1 0 5z"/></svg></span>
      <span class="contact__text">718 West Halden Lane,<br>Dania Beach, FL 33019</span>
    </li>
    <li class="contact contact--phone">
      <span class="contact__icon"><svg viewBox="0 0 24 24"><path d="M2 9c0-3 5-5 10-5s10 2 10 5v2h-5V8H7v3H2zM6 12h12l3 8H3z"/></svg></span>
      <span class="contact__text">954-382-7146</span>
    </li>
    <li class="contact contact--fax">
      <span class="contact__icon"><svg viewBox="0 0 24 24"><path d="M6 2h12v5H6zM3 8h18v9h-3v5H6v-5H3zm5 7v5h8v-5z"/></svg></span>
      <span class="contact__text">954:382-7139</span>
    </li>
    <li class="contact contact--cell">
      <span class="contact__icon"><svg viewBox="0 0 24 24"><path d="M6.6 10.8a15 15 0 0 0 6.6 6.6l2.2-2.2c.3-.3.7-.4 1-.2 1.1.4 2.3.6 3.6.6.6 0 1 .4 1 1V20c0 .6-.4 1-1 1A17 17 0 0 1 3 4c0-.6.4-1 1-1h3.5c.6 0 1 .4 1 1 0 1.3.2 2.5.6 3.6.1.3 0 .7-.2 1z"/></svg></span>
      <span class="contact__text">954-451-8320</span>
    </li>
    <li class="contact contact--email">
      <span class="contact__icon"><svg viewBox="0 0 24 24"><path d="M3 4l9 8 9-8v16H3z"/></svg></span>
      <span class="contact__text">212@corvellamarine.com</span>
    </li>
    <li class="contact contact--web">
      <span class="contact__icon"><svg viewBox="0 0 24 24"><path d="M12 2a10 10 0 1 0 0 20 10 10 0 0 0 0-20zm0 2c1 1.2 1.8 3 2.1 5H9.9C10.2 7 11 5.2 12 4zM4.3 11h3.5a17 17 0 0 0 0 2H4.3a8 8 0 0 1 0-2zm5.6 0h4.2a15 15 0 0 1 0 2H9.9a15 15 0 0 1 0-2zm6.3 0h3.5a8 8 0 0 1 0 2h-3.5a17 17 0 0 0 0-2zM9.9 15h4.2c-.3 2-1.1 3.8-2.1 5-1-1.2-1.8-3-2.1-5z"/></svg></span>
      <span class="contact__text">corvellamarine.com</span>
    </li>
  </ul>
</section>

<section class="card card--back" aria-label="Business card back">
  <svg class="card__shapes" viewBox="0 0 263 430" aria-hidden="true">
    <polygon class="orange" points="0,0 17,0 152,27 61,80"/>
    <polygon class="navy" points="17,0 200,0 152,27"/>
    <polygon class="orange" points="0,430 30,391 60,409 17,430"/>
    <polygon class="navy" points="17,430 60,409 97,430"/>
  </svg>
  <span class="back-mark"></span>
  <p class="back-name">CORVELLA MARINE</p>
</section>

</body>
</html>
```